Design of an attractive membership brochure/membership card for an Electrical Business

Hi, we are an electrical business based in Sydney, Australia.

Our design's aim is to attract and target new customers into using our business as a repeat for anything electrical in their home. We would be handing this out to them after a job is completed and they're happy with the service.
We're thinking of a brochure, possibly additional membership cards with personalized number ID's for each client.

Open to ideas, but some of the things we want to include on our brochure are perks of why the client should sign up with us as a lifetime client
- Discounted emergency call out fees outside of normal hours
- Lifetime membership price, one time payment
- Exclusive 10% member discount on all future jobs
- Priority on any during business hour jobs or emergencies

If any other questions please don't hesitate to reach out.
We've attached our logo for reference for the mock designs.
Our website
https://brightwirecrew.com.au/

```html
<!DOCTYPE html>
<html lang="en">
<head>
<meta charset="utf-8">
<title>Brightwire Crew – Membership Flyer and VIP Cards</title>
<link href="https://fonts.googleapis.com/css2?family=Poppins:wght@300;400;500;600;700;800&display=swap" rel="stylesheet">
<style>
  :root {
    --red: #e0291f;
    --red-band: #d93a26;
    --ink: #1e1516;
    --panel: #241a1c;
    --white: #ffffff;
    --stage: #b4b4b4;
    --text-dark: #2a2223;
  }
  * { box-sizing: border-box; margin: 0; padding: 0; }
  html, body { width: 800px; height: 1200px; overflow: hidden; }
  body { background: var(--stage); font-family: "Poppins", sans-serif; position: relative; }

  .flyer {
    position: absolute; left: 90px; top: 80px;
    width: 748px; height: 967px; background: var(--white);
    transform: scale(0.829); transform-origin: 0 0;
    box-shadow: 4px 6px 10px rgba(0,0,0,.35); overflow: hidden;
  }
  .abs { position: absolute; }
  .brand-name { color: var(--red); font-weight: 800; font-size: 30px; line-height: 1; letter-spacing: 1px; }
  .flyer .brand-name { left: 45px; top: 58px; }
  .flyer-title { left: 44px; top: 122px; color: var(--red); font-weight: 800; font-size: 47px; line-height: 41px; letter-spacing: .5px; }
  .location-bar { left: 0; top: 218px; width: 270px; height: 30px; background: var(--ink); color: var(--white);
    font-weight: 300; font-size: 21px; letter-spacing: 5px; padding-left: 45px; line-height: 30px; }
  .tagline { left: 43px; top: 264px; width: 300px; font-weight: 600; font-size: 14px; line-height: 17px; color: var(--ink); }

  .red-band { left: 0; top: 340px; width: 748px; height: 327px; background: var(--red-band); }
  .section-title { font-weight: 700; font-size: 22px; line-height: 1; }
  .about .section-title { color: var(--white); }
  .about { left: 42px; top: 360px; width: 300px; }
  .rule { width: 38px; height: 3px; margin: 7px 0 14px; }
  .about .rule { background: var(--ink); }
  .about p { color: var(--white); font-size: 12.4px; line-height: 14.6px; margin-bottom: 14px; }

  .dark-panel { left: 353px; top: 0; width: 360px; height: 697px; background: var(--panel); }
  .room-photo { left: 353px; top: 0; width: 360px; height: 345px;
    background: radial-gradient(circle at 30% 22%, #b8782e 0, #6a3d1c 16%, transparent 34%),
                radial-gradient(circle at 65% 30%, #a0632a 0, transparent 22%),
                linear-gradient(180deg, #1e2a2a 0%, #3b2a1e 55%, var(--panel) 100%); }
  .why { left: 390px; top: 360px; }
  .why .section-title { color: var(--white); }
  .why .rule { background: var(--red); }
  .perk { position: absolute; width: 130px; height: 99px; border: 1px solid var(--red); border-radius: 8px;
    color: var(--white); font-size: 14px; line-height: 16px; text-align: center; padding-top: 31px; }
  .perk strong { font-weight: 700; }
  .perk-icon { position: absolute; left: 45px; top: -21px; width: 40px; height: 40px; border-radius: 50%;
    background: var(--white); border: 3px solid var(--red); display: flex; align-items: center; justify-content: center; }

  .job-photo { top: 700px; width: 136px; height: 156px; border-radius: 10px; border: 2px solid var(--ink); }
  .job-photo.bedroom { left: 41px; background: linear-gradient(160deg, #e6d5b8, #b08a5e 60%, #6e4f36); }
  .job-photo.lounge { left: 185px; background: linear-gradient(160deg, #7a5636, #b78c5c 55%, #3e2a1c); }
  .call { left: 38px; top: 876px; font-weight: 700; font-size: 26px; color: var(--ink); display: flex; align-items: center; gap: 6px; white-space: nowrap; }
  .email { left: 40px; top: 916px; font-weight: 700; font-size: 16px; color: var(--ink); display: flex; align-items: center; gap: 6px; }

  .services { left: 353px; top: 720px; width: 380px; }
  .services .section-title { color: var(--ink); }
  .service-list { position: absolute; top: 48px; list-style: none; font-size: 12.5px; color: var(--text-dark); line-height: 14px; }
  .service-list li { display: flex; gap: 5px; height: 27px; }
  .service-list li.two { height: 27px; }
  .service-list .plain { padding-left: 14px; }
  .tick { flex: none; margin-top: 1px; }

  .card { position: absolute; top: 910px; width: 540px; height: 308px; background: var(--panel);
    transform: scale(0.685); transform-origin: 0 0; box-shadow: 4px 6px 10px rgba(0,0,0,.35); color: var(--white); }
  .card.front { left: 20px; }
  .card.back { left: 410px; }
  .vip-badge { left: 108px; top: 42px; width: 68px; height: 54px; background: var(--red); border-radius: 8px;
    font-weight: 800; font-size: 34px; line-height: 54px; text-align: center; }
  .card-divider { left: 225px; top: 42px; width: 1px; height: 54px; background: #5a4d4f; }
  .card.front .brand-name { left: 248px; top: 54px; }
  .member-field { left: 40px; top: 141px; width: 462px; height: 40px; background: var(--white); border-radius: 6px;
    color: var(--text-dark); font-size: 14px; line-height: 40px; padding-left: 13px; }
  .member-field span { display: inline-block; width: 2px; height: 26px; background: var(--red); vertical-align: middle; margin-left: 4px; }
  .member-name { left: 0; top: 216px; width: 540px; text-align: center; font-size: 22px; font-weight: 400; }
  .member-name b { color: var(--red); font-weight: 600; }
  .card-contacts { left: 0; top: 253px; width: 540px; display: flex; justify-content: center; gap: 14px; font-size: 12px; }
  .card-contacts span { display: flex; align-items: center; gap: 3px; }
  .card.back .brand-name { left: 0; width: 540px; text-align: center; top: 48px; }
  .membership-title { left: 0; top: 125px; width: 540px; text-align: center; font-size: 52px; font-weight: 800; letter-spacing: .5px; }
  .membership-title .vip { color: var(--red); font-weight: 300; margin-right: 14px; }
  .card-url { left: 0; top: 246px; width: 540px; text-align: center; font-size: 16px; letter-spacing: 2px; font-weight: 500; }
  .card-url b { color: var(--red); font-weight: 700; }
</style>
</head>
<body>

<section class="flyer">
  <div class="abs brand-name">BRIGHTWIRE CREW</div>
  <h1 class="abs flyer-title">ELECTRICAL<br>BUSINESS</h1>
  <div class="abs location-bar">SYDNEY BASED</div>
  <p class="abs tagline">Specialising in electrical maintenance work for residential, commercial, strata &amp; real estate clients</p>

  <div class="abs red-band"></div>
  <div class="abs about">
    <h2 class="section-title">ABOUT US</h2>
    <div class="rule"></div>
    <p>Brightwire Crew is a Sydney-based electrical business specialising in electrical maintenance work for residential, commercial, strata and real estate clients. It began with two mates with a strong desire to change the image of tradies and provide exceptional service. As a team of electricians based in the Inner West of Sydney, we understand the need of everyday people struggling to find good, reliable and trustworthy electricians.</p>
    <p>At Brightwire Crew, we have high expectations of ourselves and strive to improve every day. We're always available around the clock to provide professional advice or give a helping hand when in need.</p>
  </div>

  <div class="abs dark-panel"></div>
  <div class="abs room-photo" role="img" aria-label="Dark lounge room lit by glowing amber pendant globe lights"></div>
  <div class="abs why">
    <h2 class="section-title">WHY CHOOSE US</h2>
    <div class="rule"></div>
  </div>
  <div class="abs" style="left:389px;top:427px;">
    <div class="perk" style="left:0;top:0;">
      <div class="perk-icon"><svg width="18" height="18" viewBox="0 0 24 24"><path fill="#1e1516" d="M6.6 10.8a15 15 0 0 0 6.6 6.6l2.2-2.2c.3-.3.7-.4 1-.2 1.1.4 2.3.6 3.6.6.6 0 1 .4 1 1V20c0 .6-.4 1-1 1A17 17 0 0 1 3 4c0-.6.4-1 1-1h3.5c.6 0 1 .4 1 1 0 1.3.2 2.5.6 3.6.1.3 0 .7-.2 1z"/></svg></div>
      Discounted emergency call out fees outside of normal hours
    </div>
    <div class="perk" style="left:158px;top:0;">
      <div class="perk-icon"><svg width="18" height="18" viewBox="0 0 24 24"><rect x="2" y="5" width="20" height="14" rx="2" fill="#1e1516"/><circle cx="8" cy="11" r="2" fill="#fff"/><rect x="12" y="9" width="7" height="1.6" fill="#fff"/><rect x="12" y="12.5" width="5" height="1.6" fill="#fff"/><rect x="5" y="14.5" width="6" height="1.6" fill="#fff"/></svg></div>
      Lifetime membership price, one time payment
    </div>
    <div class="perk" style="left:0;top:135px;">
      <div class="perk-icon"><svg width="18" height="18" viewBox="0 0 24 24"><path fill="#1e1516" d="M12 2h8a2 2 0 0 1 2 2v8L12 22 2 12z"/><circle cx="17" cy="7" r="1.8" fill="#fff"/><text x="8" y="16" font-size="8" fill="#fff" font-family="Poppins, sans-serif" font-weight="700">$</text></svg></div>
      Exclusive <strong>10% member discount</strong> on all future jobs
    </div>
    <div class="perk" style="left:158px;top:135px;">
      <div class="perk-icon"><svg width="18" height="18" viewBox="0 0 24 24"><path fill="#1e1516" d="M9 3h6a2 2 0 0 1 2 2v2h3a2 2 0 0 1 2 2v10a2 2 0 0 1-2 2H4a2 2 0 0 1-2-2V9a2 2 0 0 1 2-2h3V5a2 2 0 0 1 2-2zm0 4h6V5H9z"/><rect x="2" y="12" width="20" height="1.6" fill="#fff"/></svg></div>
      Priority on any during business hour jobs or emergencies
    </div>
  </div>

  <div class="abs job-photo bedroom" role="img" aria-label="Bright hotel-style bedroom with bedside lamps"></div>
  <div class="abs job-photo lounge" role="img" aria-label="Warm lit lounge with armchair and floor lamp"></div>
  <div class="abs call">Call us
    <svg width="22" height="22" viewBox="0 0 24 24"><path fill="none" stroke="#e0291f" stroke-width="2.2" d="M6.6 10.8a15 15 0 0 0 6.6 6.6l2.2-2.2c.3-.3.7-.4 1-.2 1.1.4 2.3.6 3.6.6.6 0 1 .4 1 1V20c0 .6-.4 1-1 1A17 17 0 0 1 3 4c0-.6.4-1 1-1h3.5c.6 0 1 .4 1 1 0 1.3.2 2.5.6 3.6.1.3 0 .7-.2 1z"/></svg>0400 517 238</div>
  <div class="abs email">
    <svg width="14" height="10" viewBox="0 0 14 10"><rect width="14" height="10" fill="#e0291f"/><path d="M0 0l7 6 7-6" stroke="#fff" fill="none"/></svg>services@brightwirecrew.com.au</div>

  <div class="abs services">
    <h2 class="section-title">OUR SERVICES</h2>
    <ul class="service-list" style="left:0;">
      <li><svg class="tick" width="12" height="12" viewBox="0 0 12 12"><rect x=".6" y="1.6" width="9.5" height="9.5" fill="none" stroke="#e0291f" stroke-width="1.3"/><path d="M3 6l2.4 2.4L11.4 1.5" fill="none" stroke="#e0291f" stroke-width="1.6"/></svg>Light Installation</li>
      <li><svg class="tick" width="12" height="12" viewBox="0 0 12 12"><rect x=".6" y="1.6" width="9.5" height="9.5" fill="none" stroke="#e0291f" stroke-width="1.3"/><path d="M3 6l2.4 2.4L11.4 1.5" fill="none" stroke="#e0291f" stroke-width="1.6"/></svg>Switchboard Install,<br>Upgrade &amp; Repair</li>
      <li><svg class="tick" width="12" height="12" viewBox="0 0 12 12"><rect x=".6" y="1.6" width="9.5" height="9.5" fill="none" stroke="#e0291f" stroke-width="1.3"/><path d="M3 6l2.4 2.4L11.4 1.5" fill="none" stroke="#e0291f" stroke-width="1.6"/></svg>Power Outlets</li>
      <li><svg class="tick" width="12" height="12" viewBox="0 0 12 12"><rect x=".6" y="1.6" width="9.5" height="9.5" fill="none" stroke="#e0291f" stroke-width="1.3"/><path d="M3 6l2.4 2.4L11.4 1.5" fill="none" stroke="#e0291f" stroke-width="1.6"/></svg>Surge Protection</li>
      <li><svg class="tick" width="12" height="12" viewBox="0 0 12 12"><rect x=".6" y="1.6" width="9.5" height="9.5" fill="none" stroke="#e0291f" stroke-width="1.3"/><path d="M3 6l2.4 2.4L11.4 1.5" fill="none" stroke="#e0291f" stroke-width="1.6"/></svg>24/7 Emergency Services</li>
      <li><svg class="tick" width="12" height="12" viewBox="0 0 12 12"><rect x=".6" y="1.6" width="9.5" height="9.5" fill="none" stroke="#e0291f" stroke-width="1.3"/><path d="M3 6l2.4 2.4L11.4 1.5" fill="none" stroke="#e0291f" stroke-width="1.6"/></svg>Electric Hot Water Repairs</li>
    </ul>
    <ul class="service-list" style="left:198px;">
      <li><svg class="tick" width="12" height="12" viewBox="0 0 12 12"><rect x=".6" y="1.6" width="9.5" height="9.5" fill="none" stroke="#e0291f" stroke-width="1.3"/><path d="M3 6l2.4 2.4L11.4 1.5" fill="none" stroke="#e0291f" stroke-width="1.6"/></svg>EV Electric Vehicle<br>Charging Stations</li>
      <li><svg class="tick" width="12" height="12" viewBox="0 0 12 12"><rect x=".6" y="1.6" width="9.5" height="9.5" fill="none" stroke="#e0291f" stroke-width="1.3"/><path d="M3 6l2.4 2.4L11.4 1.5" fill="none" stroke="#e0291f" stroke-width="1.6"/></svg>Level 2 ASP</li>
      <li><svg class="tick" width="12" height="12" viewBox="0 0 12 12"><rect x=".6" y="1.6" width="9.5" height="9.5" fill="none" stroke="#e0291f" stroke-width="1.3"/><path d="M3 6l2.4 2.4L11.4 1.5" fill="none" stroke="#e0291f" stroke-width="1.6"/></svg>Smoke Alarms</li>
      <li><svg class="tick" width="12" height="12" viewBox="0 0 12 12"><rect x=".6" y="1.6" width="9.5" height="9.5" fill="none" stroke="#e0291f" stroke-width="1.3"/><path d="M3 6l2.4 2.4L11.4 1.5" fill="none" stroke="#e0291f" stroke-width="1.6"/></svg>Ceiling &amp; Exhaust Fans</li>
      <li class="plain">Real estate, Strata<br>and Commercial</li>
    </ul>
  </div>
</section>

<section class="card front">
  <div class="abs vip-badge">VIP</div>
  <div class="abs card-divider"></div>
  <div class="abs brand-name">BRIGHTWIRE CREW</div>
  <div class="abs member-field">VIP Membership No.<span></span></div>
  <div class="abs member-name"><b>MARCUS</b> HALE</div>
  <div class="abs card-contacts">
    <span><svg width="10" height="10" viewBox="0 0 24 24"><path fill="#e0291f" d="M6.6 10.8a15 15 0 0 0 6.6 6.6l2.2-2.2c.3-.3.7-.4 1-.2 1.1.4 2.3.6 3.6.6.6 0 1 .4 1 1V20c0 .6-.4 1-1 1A17 17 0 0 1 3 4c0-.6.4-1 1-1h3.5c.6 0 1 .4 1 1 0 1.3.2 2.5.6 3.6.1.3 0 .7-.2 1z"/></svg>0400 517 238</span>
    <span><svg width="11" height="8" viewBox="0 0 14 10"><rect width="14" height="10" fill="#e0291f"/><path d="M0 0l7 6 7-6" stroke="#241a1c" fill="none"/></svg>services@brightwirecrew.com.au</span>
    <span><svg width="10" height="10" viewBox="0 0 12 12"><circle cx="6" cy="6" r="5" fill="none" stroke="#e0291f" stroke-width="1.4"/><path d="M1 6h10M6 1c-2.5 3-2.5 7 0 10M6 1c2.5 3 2.5 7 0 10" fill="none" stroke="#e0291f"/></svg>www.brightwirecrew.com.au</span>
  </div>
</section>

<section class="card back">
  <div class="abs brand-name">BRIGHTWIRE CREW</div>
  <div class="abs membership-title"><span class="vip">VIP</span>MEMBERSHIP</div>
  <div class="abs card-url">www.<b>brightwirecrew</b>.com.au</div>
</section>

</body>
</html>
```